Website - Tides Of Bloom

We are catalysts of change in people's lives.
We work with individuals and professionals to bring about instant substantial & transforming change in their lives.
We provide one-on-one lifestyle coaching by an experienced practitioner.
Our existing website is www.tidesofbloom.biz & this site contains our the basis for the content of our desired new project, so please examine this carefully.
We require a professional and captivating website that will instantly impress, engage invite our readers to click & invest their lives.
Our services do not come cheap, but are second to none.
Our website must be contemporary whilst reflecting indisputable class & ultra-confidence in the success of our work.
Target Market(s)
Those who seek to want to change in their lives. Those aged primarily between 30 and 50 years of age, male or female.
Industry/Entity Type
Work
Look and feel

```html
<!DOCTYPE html>
<html lang="en">
<head>
<meta charset="utf-8">
<title>Tides Of Bloom</title>
<link href="https://fonts.googleapis.com/css2?family=Mulish:wght@300;400;600&display=swap" rel="stylesheet">
<style>
:root{
  --bar:#2f2f3b;
  --page:#edebe5;
  --ink:#4a4a4a;
  --heading:#5a5a5a;
  --accent:#f0883e;
  --button:#f4a964;
  --news:#3a8aa8;
  --menu:#f1ece7;
  --white:#ffffff;
}
*{margin:0;padding:0;box-sizing:border-box}
html,body{width:1200px;height:870px;overflow:hidden}
body{position:relative;background:var(--page);font-family:"Mulish",sans-serif;color:var(--ink)}
.site-header{position:absolute;left:0;top:0;width:1200px;height:113px;background:var(--bar)}
.brand{position:absolute;left:136px;top:30px;display:flex;align-items:center;gap:10px;color:#c9c9cf;font-size:30px;font-weight:600}
.brand-dot{width:34px;height:34px;border-radius:50%;background:#c9c9cf}
.call{position:absolute;left:596px;top:31px;color:var(--white);font-size:16px}
.call strong{color:var(--accent);font-weight:400;font-size:21px}
.search{position:absolute;left:862px;top:23px;width:179px;height:26px;border-bottom:1px solid #777}
.search svg{position:absolute;right:0;top:4px}
.main-nav{position:absolute;top:73px;left:0;width:1200px}
.main-nav a{position:absolute;color:#e6e6e6;font-size:15px;letter-spacing:2.3px;text-decoration:none}
.main-nav .active{border-bottom:2px solid var(--accent);padding-bottom:4px}
.dropdown{position:absolute;left:735px;top:97px;width:156px;height:142px;background:var(--menu);box-shadow:0 2px 5px rgba(0,0,0,.15);padding:0 12px;z-index:2}
.dropdown a{display:block;height:40px;line-height:45px;border-bottom:1px solid #bdb7b2;font-size:13px;letter-spacing:1.4px;color:#444;text-decoration:none}
.dropdown a:first-child{height:42px;line-height:43px}
.hero{position:absolute;left:23px;top:142px;width:1152px;height:407px;background:linear-gradient(90deg,#f3c9a0 0%,#f1d6bb 35%,#ead7c4 55%,#c99a70 75%,#9a6a43 100%);box-shadow:0 1px 4px rgba(0,0,0,.15)}
.hero-copy{position:absolute;left:159px;top:226px}
.hero-copy h1{font-weight:300;font-size:45px;color:#555;letter-spacing:.5px;line-height:1}
.hero-copy ul{list-style:none;margin-top:14px}
.hero-copy li{font-size:19px;font-weight:300;color:#4a4a4a;line-height:28px;padding-left:18px;position:relative}
.hero-copy li::before{content:"";position:absolute;left:3px;top:10px;width:8px;height:8px;border:2px solid #666;border-radius:50%}
.btn{position:absolute;left:159px;top:391px;width:242px;height:48px;background:var(--button);color:var(--white);font-size:21px;line-height:48px;padding-left:23px;text-decoration:none}
.welcome{position:absolute;left:140px;top:585px;width:570px}
.welcome h2{font-weight:300;font-size:28px;color:var(--heading);margin-bottom:6px}
.welcome p{font-size:14px;line-height:18px;margin-bottom:10px}
.divider{position:absolute;left:741px;top:600px;height:176px;border-left:1px dotted #999}
.news{position:absolute;left:780px;top:593px;width:262px}
.news h3{font-weight:400;font-size:17px;color:var(--news);margin-bottom:6px}
.news-item{position:relative;height:84px;padding-left:51px}
.date{position:absolute;left:0;top:0;width:43px;height:52px;background:#f2a55c;border:2px solid #d8d8d8;border-radius:3px;color:var(--white);text-align:center;font-size:15px;line-height:17px;padding-top:7px}
.news-item h4{font-size:13px;font-weight:600;margin-bottom:4px}
.news-item p{font-size:13px;line-height:15px}
.more{position:absolute;right:0;bottom:18px;font-size:13px}
.site-footer{position:absolute;left:0;top:817px;width:1200px;height:53px;background:var(--bar);color:var(--white);font-size:13px}
.copy{position:absolute;left:141px;top:18px}
.foot-nav{position:absolute;right:159px;top:19px}
.foot-nav a{color:var(--white);text-decoration:none}
</style>
</head>
<body>
<header class="site-header">
  <div class="brand"><span class="brand-dot"></span>Tides Of Bloom</div>
  <div class="call">Call Now: <strong>+61 02 5550 1294</strong></div>
  <div class="search"><svg width="16" height="16" viewBox="0 0 16 16"><circle cx="6" cy="6" r="4.5" fill="none" stroke="#aaa" stroke-width="2"/><line x1="9.5" y1="9.5" x2="15" y2="15" stroke="#aaa" stroke-width="2.5"/></svg></div>
  <nav class="main-nav">
    <a style="left:542px">HOME</a>
    <a style="left:635px">ABOUT</a>
    <a class="active" style="left:737px">SERVICES</a>
    <a style="left:864px">NEWS</a>
    <a style="left:956px">CONTACT</a>
  </nav>
</header>
<div class="dropdown">
  <a>Business</a><a>Individuals</a><a>Others</a>
</div>
<section class="hero" role="img" aria-label="Rock climber scaling a cliff against a warm sunset sky"></section>
<div class="hero-copy">
  <h1>CHANGE IS YOURS</h1>
  <ul>
    <li>More choices about your behaviours and emotions</li>
    <li>Improve your relationships and the ways you communicate</li>
    <li>Change better results through becoming a greater thinker</li>
  </ul>
</div>
<a class="btn">LEARN MORE</a>
<section class="welcome">
  <h2>Welcome to our website:</h2>
  <p>Our clients experience their desired instant &amp; permanent transformation, emerging from our consultations ready to take on their world from a vastly different paradigm.</p>
  <p>At Tides Of Bloom, our Master Practitioner will inspire you, shifting your perspective &amp; facilitating your mind with the freedom to realise your dreams.</p>
  <p>Join Martin Hale, Clara Voss, R.J. Linwood, Dex Harmon, Paul Greer, Nina Sorell and hundreds of thousands of others who are achieving the life changing, consistent results you are dreaming of now.</p>
</section>
<div class="divider"></div>
<aside class="news">
  <h3>Latest News:</h3>
  <div class="news-item">
    <div class="date">11<br>Dec</div>
    <h4>Title of News:</h4>
    <p>Tides Of Bloom have worked with CEO's &amp; business owners throughout Australia .</p>
    <span class="more">+ More</span>
  </div>
  <div class="news-item">
    <div class="date">10<br>Dec</div>
    <h4>Title of News:</h4>
    <p>Tides Of Bloom have worked with CEO's &amp; business owners throughout Australia .</p>
    <span class="more">+ More</span>
  </div>
</aside>
<footer class="site-footer">
  <div class="copy">Copyright © 2013 Tides Of Bloom | All Rights Reserved</div>
  <nav class="foot-nav"><a>Home</a> &nbsp;I&nbsp; <a>About</a> &nbsp;I&nbsp; <a>Services</a> &nbsp;I&nbsp; <a>News</a> &nbsp;I&nbsp; <a>Contact Us</a></nav>
</footer>
</body>
</html>
```